Steadfast Support! Virtual Assistant business needs a Website

I have started an online business called "Steadfast Support". I offer all the same types of services as a typical Personal Assistant, only remotely. For example, document formatting and editing (word, powerpoint, excel etc.), email and calendar management, appointments and bookings, document creation, reports, travel and event management and so on.

I already have a logo ready to go, however I have yet to finalise the copy for the site, so if you could create the pages with pictures, and I can fill in the wording at a later date.

Target Market(s)

Anyone who is overloaded at work and needs someone to take the admin work off their hands.

Number of Pages Required

4 page

Font styles to use
Sans Serif
Script
Other font styles liked:
• Gotham Medium is used in my font

Colors

Designer to choose colors to be used in the design.

Requirements
Must have
• Home Page
• About Page
• Pricing Page
• Contact Page
Nice to have
• Pictures and a professional design, I like white space and simple design.
Should not have
• cartoons or anything unprofessional looking.

```html
<!DOCTYPE html>
<html lang="en">
<head>
<meta charset="UTF-8">
<title>Steadfast Support — Home</title>
<link rel="stylesheet" href="https://fonts.googleapis.com/css2?family=Montserrat:ital,wght@0,400;0,500;0,600;1,400;1,500&display=swap">
<style>
  :root {
    --brand-blue: #1f5fa8;
    --brand-navy: #1d3a66;
    --ink: #3a3f47;
    --muted: #6d737c;
    --rule: #c9ced6;
    --white: #ffffff;
    --hero-overlay: rgba(40, 44, 52, 0.62);
  }
  * { box-sizing: border-box; margin: 0; padding: 0; }
  html, body {
    width: 1200px; height: 900px; overflow: hidden;
    background: var(--white);
    font-family: "Montserrat", Arial, sans-serif;
    color: var(--ink);
  }
  .page { width: 1200px; height: 900px; position: relative; overflow: hidden; }

  /* Header */
  .site-header {
    height: 84px; display: flex; align-items: center; justify-content: space-between;
    padding: 0 110px 0 110px; background: var(--white);
  }
  .brand { display: flex; align-items: center; gap: 10px; }
  .brand-dot { width: 30px; height: 30px; border-radius: 50%; background: var(--brand-blue); }
  .brand-name { font-size: 19px; font-weight: 600; color: var(--brand-navy); letter-spacing: 0.5px; }
  .main-nav { display: flex; align-items: center; gap: 40px; }
  .nav-link { font-size: 13px; color: var(--ink); text-decoration: none; position: relative; padding: 6px 0; }
  .nav-link.is-active { color: var(--brand-blue); }
  .nav-link.is-active::after {
    content: ""; position: absolute; left: -4px; right: -4px; bottom: -2px;
    height: 2px; background: var(--brand-blue);
  }
  .login-button {
    display: flex; align-items: center; gap: 7px;
    border: 1.5px solid var(--brand-blue); color: var(--brand-blue);
    font-size: 13px; font-weight: 600; padding: 8px 22px; text-decoration: none;
  }

  /* Hero */
  .hero { position: relative; height: 470px; }
  .hero-photo {
    position: absolute; inset: 0;
    background: linear-gradient(100deg, #8a8f93 0%, #b9b4a8 45%, #d8d6d0 70%, #a9b0b6 100%);
  }
  .hero-photo::after { content: ""; position: absolute; inset: 0; background: var(--hero-overlay); }
  .hero-content { position: absolute; left: 140px; top: 105px; width: 440px; color: var(--white); }
  .hero-kicker { font-size: 14px; font-style: italic; margin-bottom: 8px; }
  .hero-title { font-size: 34px; font-weight: 500; font-style: italic; line-height: 1.15; margin-bottom: 16px; }
  .hero-text { font-size: 12px; font-style: italic; line-height: 1.6; margin-bottom: 26px; opacity: 0.95; }
  .hero-actions { display: flex; gap: 12px; }
  .btn { font-size: 12px; font-style: italic; padding: 9px 26px; text-decoration: none; }
  .btn-solid { background: var(--white); color: var(--brand-blue); }
  .btn-outline { border: 1px solid var(--white); color: var(--white); }

  /* About */
  .about { text-align: center; padding-top: 48px; }
  .about-mark { width: 44px; height: 44px; border-radius: 50%; background: var(--brand-blue); margin: 0 auto 14px; }
  .about-heading {
    display: flex; align-items: center; justify-content: center; gap: 18px;
    font-size: 28px; font-weight: 500; font-style: italic; color: var(--brand-navy); margin-bottom: 22px;
  }
  .about-heading::before, .about-heading::after { content: ""; width: 60px; height: 1px; background: var(--rule); }
  .about-text { width: 640px; margin: 0 auto; font-size: 12px; font-style: italic; line-height: 1.75; color: var(--muted); }
</style>
</head>
<body>
<div class="page">
  <header class="site-header">
    <div class="brand">
      <span class="brand-dot"></span>
      <span class="brand-name">STEADFAST SUPPORT</span>
    </div>
    <nav class="main-nav">
      <a class="nav-link is-active" href="#">Home</a>
      <a class="nav-link" href="#">About</a>
      <a class="nav-link" href="#">Pricing</a>
      <a class="nav-link" href="#">Contact</a>
      <a class="login-button" href="#">
        <svg width="14" height="12" viewBox="0 0 14 12" aria-hidden="true">
          <path d="M1 6h8M6 3l3 3-3 3" fill="none" stroke="currentColor" stroke-width="1.5"/>
          <path d="M9 1h4v10H9" fill="none" stroke="currentColor" stroke-width="1.5"/>
        </svg>
        Login
      </a>
    </nav>
  </header>

  <section class="hero">
    <div class="hero-photo" role="img" aria-label="Photo of a smiling woman working at a laptop in a bright office"></div>
    <div class="hero-content">
      <p class="hero-kicker">I offer all the same types of services as a</p>
      <h1 class="hero-title">Typical Personal Assistant</h1>
      <p class="hero-text">Hand over the emails, documents and bookings that fill your day, and get back the hours you need for growing your business and the things that matter most.</p>
      <div class="hero-actions">
        <a class="btn btn-solid" href="#">Contact Us</a>
        <a class="btn btn-outline" href="#">Get Started</a>
      </div>
    </div>
  </section>

  <section class="about">
    <div class="about-mark"></div>
    <h2 class="about-heading">About Us</h2>
    <p class="about-text">We take the admin off your desk so you can focus on the work that matters. From inbox and calendar care to reports, bookings and travel plans, every task is handled with care, speed and discretion, wherever you are based.</p>
  </section>
</div>
</body>
</html>
```